Breezeway Climate Business Card Design

Design new, 2 sides, business cards for a residential and light commercial heating, air conditioning contractor.

Target Market(s)

Homeowners, small businesses

Industry/Entity Type

Business

Contact Information for Business Card

Dominic Vasquerelli
Phone - 555-214-6837
Email
Address - PO box 618
Millbrook NJ 07999
Website - www.BreezewayClimateLLC.example

Requirements
Must have
• logo, company colors, standard size with no die cut, so I can use printhaven

```html
<!DOCTYPE html>
<html lang="en">
<head>
<meta charset="utf-8">
<title>Breezeway Climate Business Card</title>
<link href="https://fonts.googleapis.com/css2?family=Roboto:wght@400;500;700&display=swap" rel="stylesheet">
<style>
  :root {
    --backdrop: #3b3b3b;
    --card: #252223;
    --accent: #f7941d;
    --brand-red: #9b2335;
    --cream: #f6e7b4;
    --text-light: #f3ecd9;
    --divider: #4a4546;
  }
  html, body {
    margin: 0;
    padding: 0;
    width: 1200px;
    height: 1000px;
    overflow: hidden;
    background: var(--backdrop);
    font-family: "Roboto", Arial, sans-serif;
  }
  .stage {
    position: relative;
    width: 1200px;
    height: 1000px;
  }
  .card {
    position: absolute;
    left: 287px;
    width: 626px;
    height: 358px;
    background: var(--card);
    box-shadow: 0 6px 18px rgba(0,0,0,0.45);
  }
  .card-front { top: 140px; }
  .card-back { top: 532px; }

  .brand-name {
    font-weight: 700;
    color: var(--cream);
    line-height: 1.05;
  }
  .brand-disc {
    border-radius: 50%;
    background: var(--brand-red);
    flex: none;
  }

  .front-brand {
    position: absolute;
    inset: 0;
    display: flex;
    align-items: center;
    justify-content: center;
    gap: 22px;
  }
  .front-brand .brand-disc { width: 96px; height: 96px; }
  .front-brand .brand-name { font-size: 50px; white-space: nowrap; }

  .back-brand {
    position: absolute;
    left: 42px;
    top: 102px;
    width: 238px;
    height: 150px;
    display: flex;
    align-items: center;
    justify-content: center;
    gap: 14px;
  }
  .back-brand .brand-disc { width: 58px; height: 58px; }
  .back-brand .brand-name { font-size: 30px; }

  .divider {
    position: absolute;
    left: 306px;
    top: 100px;
    width: 1px;
    height: 154px;
    background: var(--divider);
  }

  .contact {
    position: absolute;
    left: 333px;
    top: 102px;
    color: var(--text-light);
    font-size: 14px;
    line-height: 19px;
  }
  .contact-name {
    margin: 0 0 16px;
    font-size: 18px;
    font-weight: 500;
    color: var(--accent);
    letter-spacing: 0.2px;
  }
  .address { margin: 0 0 16px; }
  .links { list-style: none; margin: 0; padding: 0; }
  .links li {
    display: flex;
    align-items: center;
    gap: 7px;
    height: 22px;
  }
  .links svg { width: 11px; height: 11px; flex: none; fill: var(--accent); }
</style>
</head>
<body>
<div class="stage">
  <section class="card card-front">
    <div class="front-brand">
      <span class="brand-disc"></span>
      <span class="brand-name">Breezeway Climate</span>
    </div>
  </section>

  <section class="card card-back">
    <div class="back-brand">
      <span class="brand-disc"></span>
      <span class="brand-name">Breezeway<br>Climate</span>
    </div>
    <div class="divider"></div>
    <div class="contact">
      <p class="contact-name">Dominic Vasquerelli</p>
      <p class="address">PO box 618<br>Millbrook NJ 07999</p>
      <ul class="links">
        <li>
          <svg viewBox="0 0 12 12" aria-hidden="true"><path d="M2.4 0.6l2 2.1-1 1.3c0.7 1.6 2 2.9 3.6 3.6l1.3-1 2.1 2-0.9 1.9C5.2 10.5 1.5 6.8 0.5 1.5z"/></svg>
          <span>555-214-6837</span>
        </li>
        <li>
          <svg viewBox="0 0 12 12" aria-hidden="true"><path d="M0.5 2.5h11v7h-11z M0.5 2.5l5.5 4 5.5-4" stroke="#252223" stroke-width="0.8"/></svg>
          <span>info@BreezewayClimateLLC.example</span>
        </li>
        <li>
          <svg viewBox="0 0 12 12" aria-hidden="true"><circle cx="6" cy="6" r="5.5"/><path d="M0.5 6h11M6 0.5v11M3 1.6c-1.5 2.6-1.5 6.2 0 8.8M9 1.6c1.5 2.6 1.5 6.2 0 8.8" stroke="#252223" stroke-width="0.8" fill="none"/></svg>
          <span>www.BreezewayClimateLLC.example</span>
        </li>
      </ul>
    </div>
  </section>
</div>
</body>
</html>
```